Medical Device - Case Study Template

We need a TEMPLATE that we can reuse to write various case studies about the medical equipment solutions we provide. It will be a double sided letter sized with a modern design that conveys a feeling of expertise, innovation and highly personable service AND be consistent with the brand guide. The content will be divided into a few sections:

- Situation (200-250 words)
- Challenge (100-120 words)
- Solution (100-120 words)
- Results (100-120 words)
- Conclusion (100-120 words)

Additionally, there will need to be a call to action, inviting people to send an email for more information and a short "About Valtu" section (approx. 40 words).

For device picture placeholders, feel free to use any random small benchtop medical device.

```html
<!DOCTYPE html>
<html lang="en">
<head>
<meta charset="utf-8">
<title>Valtu Case Study Template and Business Cards</title>
<link href="https://fonts.googleapis.com/css2?family=Montserrat:wght@600;700;800;900&family=Barlow+Condensed:wght@400;500;600&family=Catamaran:wght@500;600&display=swap" rel="stylesheet">
<style>
:root{
  --orange:#f1812e;
  --blue:#7aa3bf;
  --ink:#555a60;
  --white:#ffffff;
  --stage:#3b3c3e;
  --stage-band:#48494b;
  --photo-light:#e4f0f9;
  --photo-mid:#8fbde3;
  --photo-deep:#3d72b0;
}
*{margin:0;padding:0;box-sizing:border-box}
html,body{width:1200px;height:1084px;overflow:hidden}
body{background:var(--stage);font-family:"Barlow Condensed",sans-serif}
.canvas{position:relative;width:1200px;height:1084px;overflow:hidden;
  background:linear-gradient(135deg,var(--stage) 0 45%,var(--stage-band) 45% 72%,var(--stage) 72%)}
.abs{position:absolute}
.page{position:absolute;top:77px;width:497px;height:701px;background:var(--white);box-shadow:4px 6px 12px rgba(0,0,0,.45);overflow:hidden}
.page-front{left:88px}
.page-back{left:615px}
.photo{position:absolute;
  background:
    radial-gradient(ellipse at 35% 30%,rgba(255,255,255,.85),rgba(255,255,255,0) 45%),
    radial-gradient(ellipse at 70% 75%,rgba(40,70,120,.55),rgba(40,70,120,0) 40%),
    linear-gradient(165deg,var(--photo-light),var(--photo-mid) 55%,var(--photo-deep))}
.body-copy{font-size:7.2px;line-height:9.1px;color:var(--ink);text-align:justify}
.body-copy p+p{margin-top:9px}
.brand{font-family:"Catamaran",sans-serif;font-weight:600;letter-spacing:1px;display:flex;align-items:center;gap:6px;line-height:1}
.brand-mark{display:inline-block;background:var(--orange)}
/* front */
.front-band-top{left:0;top:0;width:250px;height:32px;background:var(--orange)}
.front-band-left{left:0;top:0;width:32px;height:249px;background:var(--orange)}
.front-photo{left:34px;top:35px;width:430px;height:263px}
.front-blue-corner{left:247px;top:549px;width:250px;height:152px;background:var(--blue)}
.title-block{left:32px;top:302px;width:214px;height:190px;background:var(--blue);color:var(--white)}
.title-kicker{position:absolute;left:20px;top:36px;width:174px;border-top:1px solid var(--white);border-bottom:1px solid var(--white);font-family:"Catamaran",sans-serif;font-weight:500;font-size:17px;padding:2px 3px;line-height:1.2}
.title-main{position:absolute;left:20px;top:66px;font-family:"Montserrat",sans-serif;font-weight:900;font-size:43px;line-height:.98;letter-spacing:-.5px}
.front-brand{left:280px;top:420px;color:var(--blue);font-size:38px}
.front-brand .brand-mark{width:22px;height:22px}
.situation{left:0;top:492px;width:470px;height:179px;background:var(--orange);color:var(--white);padding:14px 22px 0 42px}
.section-title{font-family:"Montserrat",sans-serif;font-weight:800;font-size:17px;line-height:1}
.situation .body-copy{color:var(--white);margin-top:9px;font-size:7.5px;line-height:10px}
.situation .body-copy p+p{margin-top:8px}
/* back */
.back-band-top{right:0;top:0;width:250px;height:31px;background:var(--orange)}
.back-band-right{right:0;top:31px;width:35px;height:180px;background:var(--orange)}
.back-photo{left:0;top:35px;width:469px;height:149px}
.col{position:absolute;top:210px;width:130px}
.col-title{font-family:"Montserrat",sans-serif;font-weight:700;font-size:15px;color:var(--orange);border-bottom:1px solid var(--orange);padding-bottom:2px;margin-bottom:6px}
.conclusion{left:37px;top:409px;width:460px;height:112px;background:var(--orange);color:var(--white);padding:10px 24px 0 24px}
.conclusion .section-title{font-size:15px;font-weight:700;display:inline-block;border-bottom:1px solid var(--white);padding-bottom:2px;padding-right:18px}
.conclusion .body-copy{color:var(--white);margin-top:6px;font-size:7.4px;line-height:10px}
.conclusion .body-copy p+p{margin-top:10px}
.about{left:61px;top:537px;width:410px}
.about .col-title{display:inline-block;padding-right:16px;font-size:16px}
.about p{font-size:8.8px;line-height:12px;color:var(--blue)}
.back-brand{left:40px;top:625px;color:var(--blue);font-size:30px}
.back-brand .brand-mark{width:22px;height:22px}
.divider{left:212px;top:613px;width:2px;height:46px;background:var(--orange)}
.contact-bar{left:219px;top:613px;width:278px;height:58px;background:var(--blue);color:var(--white);font-weight:600;font-size:11px;padding:9px 0 0 20px}
.contact-row{display:flex;align-items:center;gap:8px;height:19px}
.contact-row svg{width:13px;height:13px}
/* cards */
.card-label{top:826px;color:var(--white);font-family:"Catamaran",sans-serif;font-weight:500;font-size:30px;width:400px;text-align:center}
.card{position:absolute;top:878px;width:210px;height:120px;overflow:hidden;box-shadow:2px 3px 6px rgba(0,0,0,.4)}
.card-white{background:var(--white)}
.card-blue{background:var(--blue)}
.card-name{font-family:"Catamaran",sans-serif;font-weight:600;font-size:10px;line-height:1}
.card-title{font-size:4.5px;letter-spacing:.6px;margin-top:2px}
.card-contacts{font-size:5.2px;font-weight:500;line-height:1}
.card-contacts li{list-style:none;display:flex;align-items:center;gap:4px;height:10.3px}
.card-contacts svg{width:5px;height:5px}
</style>
</head>
<body>
<div class="canvas">

  <!-- Front page -->
  <section class="page page-front">
    <div class="abs front-band-top"></div>
    <div class="abs front-band-left"></div>
    <div class="abs front-blue-corner"></div>
    <div class="photo front-photo" role="img" aria-label="Photo of a bright hospital operating room with surgical lights, table and imaging arm"></div>
    <div class="abs title-block">
      <div class="title-kicker">Medical Technology</div>
      <h1 class="title-main">CASE<br>STUDY</h1>
    </div>
    <div class="abs brand front-brand"><span class="brand-mark"></span>Valtu</div>
    <div class="abs situation">
      <h2 class="section-title">SITUATION</h2>
      <div class="body-copy">
        <p>Our client, a regional hospital group, runs twelve surgical suites across three sites and treats more than forty thousand patients each year. Aging imaging carts, monitors and surgical lights caused frequent downtime, delayed procedures and steadily rising service costs. Staff needed reliable equipment, faster support and one trusted partner able to plan upgrades without disrupting daily patient care or stretching an already tight capital budget. Previous vendors sold devices but offered little help once the boxes were opened, leaving busy teams to solve problems alone.</p>
        <p>Biomedical teams tracked repairs by hand in shared spreadsheets, spare parts were scattered between sites, and vendors rarely shared service data. Leaders wanted a clear view of every device, its age and its risk before committing to new purchases, yet no single report gave them that picture.</p>
        <p>This case study shows how a phased plan, hands-on training at the bedside and steady, personal service turned that uncertainty into clear and measurable gains for staff and patients alike.</p>
      </div>
    </div>
  </section>

  <!-- Back page -->
  <section class="page page-back">
    <div class="abs back-band-top"></div>
    <div class="abs back-band-right"></div>
    <div class="photo back-photo" role="img" aria-label="Photo of a medical equipment room with monitors, patient bed, carts and cabinets"></div>

    <div class="col" style="left:37px">
      <h3 class="col-title">CHALLENGE</h3>
      <div class="body-copy">
        <p>The client ran three hospitals with a mix of device models, manuals and service contracts gathered over fifteen years. When a monitor or imaging cart failed, repairs took nine days on average and often needed parts shipped from abroad. Surgeons lost trust in the equipment, and nurses kept spare units hidden just in case. Budgets allowed no gap in coverage, so any change had to keep every suite open while older units were retired one at a time, on a clear schedule.</p>
        <p>Staff also needed hands-on training that fit around busy shift patterns, night cover and weekend on-call rotas across all three sites.</p>
      </div>
    </div>
    <div class="col" style="left:184px">
      <h3 class="col-title">SOLUTION</h3>
      <div class="body-copy">
        <p>We began with a full audit of every device, ranking each unit by age, risk and repair history. From that list we built a three phase plan that replaced mixed fleets with standard monitors and imaging carts, delivered in small batches to avoid downtime. One service contract now covers all sites, and a dedicated engineer visits every week with spare parts kept in a locked store on site, ready for same day swaps when any unit reports a fault.</p>
        <p>Short bedside sessions trained clinical staff during regular shift handovers, with quick guides left beside every new device.</p>
      </div>
    </div>
    <div class="col" style="left:331px">
      <h3 class="col-title">RESULTS</h3>
      <div class="body-copy">
        <p>Average repair time fell from nine days to under two, and planned procedures are now rarely moved because of equipment faults. Service costs dropped by a fifth in the first year, while spare part spending became easy to forecast. Clinicians report far more confidence in their tools, and biomedical leads save hours each week on paperwork. Leaders now see every device, its age and its status in one simple dashboard shared across all three hospitals.</p>
        <p>Based on these results, the group now plans to extend the same program to two more sites next year.</p>
      </div>
    </div>

    <div class="abs conclusion">
      <h2 class="section-title">CONCLUSION</h2>
      <div class="body-copy">
        <p>A clear plan, standard equipment and a partner close at hand changed how this hospital group manages its surgical technology. Fewer delays, lower costs and trained, confident staff now support better care for every patient who comes through the doors. The phased approach proved that major upgrades need not disrupt daily work, and the weekly engineer visits built a relationship based on trust rather than emergency calls.</p>
        <p>Email our team at hello@valtumed.com to learn how a similar plan could work for your facility, your budget and your people.</p>
      </div>
    </div>

    <div class="abs about">
      <h3 class="col-title">About Valtu</h3>
      <p>Valtu supplies, installs and services medical technology for hospitals and clinics. Our engineers pair proven equipment with personal support, so care teams can spend less time on devices and more time with patients.</p>
    </div>

    <div class="abs brand back-brand"><span class="brand-mark"></span>Valtu</div>
    <div class="abs divider"></div>
    <div class="abs contact-bar">
      <div class="contact-row">
        <svg viewBox="0 0 24 24" fill="none" stroke="#fff" stroke-width="2"><path d="M5 3h4l2 5-3 2a12 12 0 0 0 6 6l2-3 5 2v4a2 2 0 0 1-2 2A18 18 0 0 1 3 5a2 2 0 0 1 2-2z"/></svg>
        <span>55 201 348 7716 | 55 201 348 7717</span>
      </div>
      <div class="contact-row">
        <svg viewBox="0 0 24 24" fill="none" stroke="#fff" stroke-width="2"><rect x="2" y="5" width="20" height="14"/><path d="M2 5l10 8 10-8"/></svg>
        <span>hello@valtumed.com | www.valtumed.com</span>
      </div>
    </div>
  </section>

  <!-- Business cards -->
  <div class="abs card-label" style="left:138px">Business Card -01</div>
  <div class="abs card-label" style="left:662px">Business Card -02</div>

  <div class="card card-white" style="left:120px">
    <svg class="abs" style="left:0;top:0" width="210" height="50" viewBox="0 0 210 50">
      <path d="M0 0H210V22H150Q138 22 132 30T114 47H0Z" fill="#f1812e"/>
      <path d="M142 28Q148 22 160 22H210V28Z" fill="#7aa3bf"/>
      <path d="M132 30Q138 22 150 22H160Q148 22 142 28L136 38Z" fill="#7aa3bf"/>
    </svg>
    <div class="abs brand" style="left:14px;top:14px;color:#fff;font-size:16px"><span class="brand-mark" style="width:10px;height:10px;background:#fff"></span>Valtu</div>
    <div class="abs" style="left:18px;top:70px;color:#333">
      <div class="card-name">Name Here</div>
      <div class="card-title">TITLE HERE</div>
      <div style="width:24px;height:1.5px;background:var(--orange);margin-top:4px"></div>
    </div>
    <ul class="abs card-contacts" style="left:112px;top:66px;color:#333">
      <li><svg viewBox="0 0 10 10"><path d="M5 0a3.5 3.5 0 0 1 3.5 3.5C8.5 6 5 10 5 10S1.5 6 1.5 3.5A3.5 3.5 0 0 1 5 0z" fill="#f1812e"/></svg>48 Harbor Lane - Westfield</li>
      <li><svg viewBox="0 0 10 10"><path d="M2 0h2l1 3-1.5 1a6 6 0 0 0 2.5 2.5L7 5l3 1v2a2 2 0 0 1-2 2A8 8 0 0 1 0 2a2 2 0 0 1 2-2z" fill="#f1812e"/></svg>+00 4410 2267 0385</li>
      <li><svg viewBox="0 0 10 10"><rect y="2" width="10" height="6" fill="#f1812e"/></svg>hello@valtumed.com</li>
      <li><svg viewBox="0 0 10 10"><path d="M2 0l6 6H5l2 4-1 .5-2-4-2 2z" fill="#f1812e"/></svg>www.valtumed.com</li>
    </ul>
  </div>

  <div class="card card-white" style="left:348px">
    <svg class="abs" style="left:0;top:0" width="210" height="50" viewBox="0 0 210 50">
      <path d="M0 0H210V47H96Q78 47 72 30T50 22H0Z" fill="#f1812e"/>
      <path d="M0 22H50Q62 22 68 30L72 36Q64 28 50 28H0Z" fill="#7aa3bf"/>
    </svg>
    <div class="abs brand" style="left:52px;top:66px;color:var(--orange);font-size:24px"><span class="brand-mark" style="width:14px;height:14px"></span>Valtu</div>
  </div>

  <div class="card card-blue" style="left:644px">
    <div class="abs brand" style="left:16px;top:14px;color:#fff;font-size:16px"><span class="brand-mark" style="width:10px;height:10px;background:#fff"></span>Valtu</div>
    <div class="abs" style="left:16px;top:50px;color:#fff">
      <div class="card-name" style="font-size:9px">Name Here</div>
      <div class="card-title" style="font-size:4px">TITLE HERE</div>
    </div>
    <ul class="abs card-contacts" style="left:16px;top:76px;color:#fff;font-size:4.4px">
      <li style="height:8px"><svg viewBox="0 0 10 10"><path d="M5 0a3.5 3.5 0 0 1 3.5 3.5C8.5 6 5 10 5 10S1.5 6 1.5 3.5A3.5 3.5 0 0 1 5 0z" fill="#fff"/></svg>48 Harbor Lane - Westfield</li>
      <li style="height:8px"><svg viewBox="0 0 10 10"><path d="M2 0h2l1 3-1.5 1a6 6 0 0 0 2.5 2.5L7 5l3 1v2a2 2 0 0 1-2 2A8 8 0 0 1 0 2a2 2 0 0 1 2-2z" fill="#fff"/></svg>+00 4410 2267 0385</li>
      <li style="height:8px"><svg viewBox="0 0 10 10"><rect y="2" width="10" height="6" fill="#fff"/></svg>hello@valtumed.com</li>
      <li style="height:8px"><svg viewBox="0 0 10 10"><path d="M2 0l6 6H5l2 4-1 .5-2-4-2 2z" fill="#fff"/></svg>www.valtumed.com</li>
    </ul>
  </div>

  <div class="card card-blue" style="left:871px">
    <div class="abs brand" style="left:24px;top:48px;color:#fff;font-size:22px"><span class="brand-mark" style="width:13px;height:13px"></span>Valtu</div>
  </div>

</div>
</body>
</html>
```